Slick Web Design for Health Care Software Company

We need a new corporate web design for our company, "CloudMedra." We specialize in web-based cloud software geared toward helping health care professionals.

Our focus for our home site is our products and services. We want potential clients and medical boards who visit our site to have an immediate sense of professionalism and know-how. Our products are innovative, easy to use, and customizable. Users should get this feel when visiting our site.

This is a link to our previous site: www.cloudmedraco.example. This site is too busy, the colors are too dark, and there's too much information in each page. When creating a design, feel free to eliminate the plethora of info present in the old site.

We have a logo and content for our site that we're going to use. For each of the 7-10 products and services, there is going to be a short 1-2 paragraph excerpt on their own page, as well as a case study related to each. Other parts that can be integrated into the site are our portfolio of clients, newsletter, and about us/contact us.

Some websites to use as general inspiration:
http://www.lessonvaltra.example/
http://www.brennet.example/
http://www.pellworthplans.example/

Target Market(s)

Health Care Professionals from Specialty Organizations and Boards

Industry/Entity Type

Health Care

Requirements
Nice to have
• Our trademark slogan is "Turn data in knowledge, knowledge into improvement." It would be pretty sweet to integrate this idea into the design of the site.

Also, BE CREATIVE. AVOID TRADITIONAL DESIGNS. Try to exemplify innovation within clarity.
Should not have
• Avoid dark backgrounds.

```html
<!DOCTYPE html>
<html lang="en">
<head>
<meta charset="utf-8">
<title>CloudMedra</title>
<link href="https://fonts.googleapis.com/css2?family=PT+Sans:wght@400;700&family=PT+Sans+Narrow:wght@400;700&display=swap" rel="stylesheet">
<style>
:root{
  --blue:#1a7cc9;
  --blue-dark:#0f5fa6;
  --text:#6a6a6a;
  --ink:#222;
  --line:#d4d8de;
  --page:#eef2fa;
  --band:#dfe8f8;
  --footer:#c3d3f3;
}
*{box-sizing:border-box;margin:0;padding:0}
html,body{width:837px;height:1200px;overflow:hidden}
body{position:relative;background:radial-gradient(ellipse at 50% 40%,#fbfcff 0%,#f1f4fb 60%,#dce5f7 100%);font-family:"PT Sans",sans-serif;color:var(--text)}
.abs{position:absolute}
.head-font{font-family:"PT Sans Narrow",sans-serif;font-weight:700;color:var(--blue);text-transform:uppercase}
/* header */
.phone{left:620px;top:7px;width:107px;text-align:right;font-size:13px;font-family:"PT Sans Narrow",sans-serif;font-weight:700;color:var(--blue)}
.social{left:685px;top:28px;display:flex;gap:5px}
.social span{width:11px;height:11px;background:var(--blue);border-radius:2px}
.brand{left:110px;top:42px;display:flex;align-items:center;gap:8px}
.brand-dot{width:30px;height:30px;border-radius:50%;background:#e3db2a}
.brand-name{font-size:28px;color:var(--ink);font-weight:400;letter-spacing:-.5px}
.nav{left:381px;top:48px;height:28px;width:346px;background:#f6f8fc;display:flex;justify-content:space-between;padding-right:8px;font-size:10px;white-space:nowrap}
.nav a{color:var(--ink);text-decoration:none;padding:0 4px;line-height:28px}
.nav a.active{background:var(--blue);color:#fff;padding:0 14px}
/* hero */
.hero{left:109px;top:89px;width:618px;height:254px;border:1px solid var(--line);background:#fff}
.hero-inner{position:absolute;left:5px;top:5px;right:5px;bottom:5px;background:linear-gradient(90deg,#ece9e6 0%,#f4f4f5 55%,#f1f2f4 100%)}
.hero-photo{position:absolute;left:0;top:0;width:306px;height:100%;background:linear-gradient(135deg,#d9cdc4 0%,#c9a98f 45%,#e6ddd6 100%)}
.slogan{left:456px;top:128px;font-size:18px;line-height:23px;white-space:nowrap}
.hero-copy{left:466px;top:186px;width:224px;font-size:10px;line-height:14px}
.btn{background:linear-gradient(#2a8fdc,var(--blue-dark));color:#fff;font-family:"PT Sans Narrow",sans-serif;font-weight:700;text-transform:uppercase;text-align:center;border:1px solid #0c4f8c;white-space:nowrap}
.hero-btn{left:467px;top:285px;width:78px;height:23px;font-size:11px;line-height:21px}
/* products */
.sec-title{font-size:16px;white-space:nowrap}
.divider-v{left:533px;top:355px;width:1px;height:600px;background:var(--line)}
.product{position:absolute;width:194px}
.product-icon{position:absolute;left:0;top:0;width:40px;height:40px}
.product-title{position:absolute;left:53px;top:15px;font-size:11.5px;white-space:nowrap}
.product-copy{position:absolute;left:0;top:44px;width:194px;font-size:8px;line-height:12.8px;text-align:justify}
.more{font-family:"PT Sans Narrow",sans-serif;font-weight:700;font-size:8px;color:#333;text-transform:uppercase;text-decoration:underline}
.product .more{position:absolute;right:0;top:122px}
.rule{height:1px;border-top:1px dashed var(--line)}
/* services */
.services{left:551px;top:388px;width:168px;list-style:none;font-size:8px}
.services li{height:19.3px;line-height:18px;border-bottom:1px dashed var(--line);display:flex;align-items:center;gap:10px;padding-left:2px;white-space:nowrap}
.services li:first-child{color:var(--blue)}
.services svg{flex:none}
/* form */
.form{left:553px;top:590px;width:174px;font-size:8px}
.field{display:flex;align-items:center;height:17px;margin-bottom:6px}
.field label{width:36px;white-space:nowrap}
.field i{width:18px;color:var(--blue);font-style:normal}
.field .input{flex:1;height:17px;background:#fff;border:1px solid var(--line)}
.field .select{display:flex;align-items:center;padding-left:12px;color:#888;position:relative}
.select b{position:absolute;right:0;top:0;width:17px;height:15px;background:#e4e9f0;display:flex;align-items:center;justify-content:center}
.field.tall{align-items:flex-start;height:58px}
.field.tall .input{height:58px}
.submit{left:659px;top:770px;width:69px;height:21px;font-size:11px;line-height:19px}
.testi-box{left:552px;top:838px;width:175px;height:120px;border:1px solid var(--line);background:#fff}
.avatar{position:absolute;left:10px;top:9px;width:32px;height:32px;background:linear-gradient(#c9d3df,#8d9aab);border-radius:4px}
.testi-name{position:absolute;left:54px;top:19px;font-size:8px;color:var(--blue)}
.testi-quote{position:absolute;left:16px;top:47px;width:152px;font-size:8px;line-height:13px;color:var(--blue)}
/* bottom band */
.band{left:0;top:972px;width:837px;height:183px;background:linear-gradient(#e3ebf9,#d5e1f6)}
.band-title{font-family:"PT Sans Narrow",sans-serif;font-weight:700;font-size:13.5px;color:var(--ink);text-transform:uppercase;white-space:nowrap}
.tiles{left:110px;top:1011px;display:grid;grid-template-columns:repeat(3,59px);gap:4px}
.tiles span{height:54px;background:#050505}
.news-date{width:44px;height:48px;background:var(--blue);color:#fff;font-family:"PT Sans Narrow",sans-serif;font-weight:700;text-align:center;line-height:1}
.news-date small{display:block;font-size:10px;padding-top:9px}
.news-date strong{font-size:17px}
.news-copy{width:119px;font-size:8px;line-height:12.8px;text-align:justify}
.about-copy{left:548px;top:1009px;width:181px;font-size:8px;line-height:12.8px;text-align:justify}
.footer{left:0;top:1155px;width:837px;height:45px;background:var(--footer)}
.copy{left:110px;top:1175px;font-size:8px;color:var(--ink)}
.sub-label{left:418px;top:1172px;font-size:10.5px}
.sub-input{left:553px;top:1168px;width:106px;height:18px;background:#fff;border:1px solid var(--line);font-size:8px;color:#999;padding:3px 8px}
.sub-btn{left:660px;top:1167px;width:67px;height:21px;font-size:11px;line-height:19px}
</style>
</head>
<body>
<header>
  <div class="abs phone">CALL- 555-0190-42</div>
  <div class="abs social"><span></span><span></span><span></span></div>
  <div class="abs brand"><span class="brand-dot"></span><span class="brand-name">CloudMedra</span></div>
  <nav class="abs nav"><a class="active">Home</a><a>About Us</a><a>Services</a><a>Prosucts</a><a>Resources</a><a>Contacts Us</a></nav>
</header>

<section class="abs hero">
  <div class="hero-inner">
    <div class="hero-photo" role="img" aria-label="Photo of a smiling senior couple"></div>
  </div>
</section>
<h1 class="abs slogan head-font">" Turn data in knowledge,<br>&nbsp;&nbsp;knowledge into improvement "</h1>
<p class="abs hero-copy">Improving the quality of health care is a necessary but daunting task. The people of CloudMedra would like to personally thank you for taking up the chal-lenge! We are excited about the opportunity to partner with you and develop highly attractive and effective health care education programs.</p>
<div class="abs btn hero-btn">View more</div>

<h2 class="abs sec-title head-font" style="left:110px;top:355px">Our Products</h2>
<div class="abs divider-v"></div>

<div class="product" style="left:110px;top:382px"><svg class="product-icon" viewBox="0 0 40 40"><circle cx="20" cy="20" r="15" fill="#9aa0a6"/><circle cx="20" cy="20" r="6" fill="#eee"/></svg><h3 class="product-title head-font">Our Products One</h3><p class="product-copy">Lorem Ipsum is simply dummy text of the printing and typesetting industry. Lorem Ipsum has been the indus-try's standard dummy text ever since the 1500s, when an unknown printer took a galley of type and scrambled it to make a type specimen book. It has survived not only five centuries,</p><span class="more" style="text-decoration:none">More</span></div>
<div class="product" style="left:322px;top:382px"><svg class="product-icon" viewBox="0 0 40 40"><rect x="6" y="6" width="22" height="28" fill="#8a9096"/><circle cx="27" cy="29" r="8" fill="#5e646a"/></svg><h3 class="product-title head-font">Our Products Two</h3><p class="product-copy">Lorem Ipsum is simply dummy text of the printing and typesetting industry. Lorem Ipsum has been the indus-try's standard dummy text ever since the 1500s, when an unknown printer took a galley of type and scrambled it to make a type specimen book. It has survived not only five centuries,</p><span class="more" style="text-decoration:none">More</span></div>
<div class="abs rule" style="left:110px;top:522px;width:194px"></div><div class="abs rule" style="left:322px;top:522px;width:194px"></div>

<div class="product" style="left:110px;top:525px"><svg class="product-icon" viewBox="0 0 40 40"><circle cx="20" cy="20" r="18" fill="#3c4248"/><circle cx="20" cy="20" r="13" fill="#777e85"/></svg><h3 class="product-title head-font">Our Products Three</h3><p class="product-copy">Lorem Ipsum is simply dummy text of the printing and typesetting industry. Lorem Ipsum has been the indus-try's standard dummy text ever since the 1500s, when an unknown printer took a galley of type and scrambled it to make a type specimen book. It has survived not only five centuries,</p><span class="more" style="text-decoration:none;top:118px">More</span></div>
<div class="product" style="left:322px;top:525px"><svg class="product-icon" viewBox="0 0 40 40"><circle cx="20" cy="20" r="18" fill="#8d9399"/><circle cx="20" cy="20" r="10" fill="none" stroke="#eee" stroke-width="4"/></svg><h3 class="product-title head-font">Our Products Four</h3><p class="product-copy">Lorem Ipsum is simply dummy text of the printing and typesetting industry. Lorem Ipsum has been the indus-try's standard dummy text ever since the 1500s, when an unknown printer took a galley of type and scrambled it to make a type specimen book. It has survived not only five centuries,</p><span class="more" style="text-decoration:none;top:118px">More</span></div>
<div class="abs rule" style="left:110px;top:663px;width:194px"></div><div class="abs rule" style="left:322px;top:663px;width:194px"></div>

<div class="product" style="left:110px;top:668px"><svg class="product-icon" viewBox="0 0 40 40"><circle cx="20" cy="20" r="18" fill="#7b8188"/><circle cx="20" cy="20" r="9" fill="#eee"/></svg><h3 class="product-title head-font">Our Products Five</h3><p class="product-copy">Lorem Ipsum is simply dummy text of the printing and typesetting industry. Lorem Ipsum has been the indus-try's standard dummy text ever since the 1500s, when an unknown printer took a galley of type and scrambled it to make a type specimen book. It has survived not only five centuries,</p><span class="more" style="text-decoration:none;top:120px">More</span></div>
<div class="product" style="left:322px;top:668px"><svg class="product-icon" viewBox="0 0 40 40"><circle cx="20" cy="20" r="16" fill="#9aa0a6"/><path d="M10 20a10 10 0 0 1 18-6" stroke="#eee" stroke-width="4" fill="none"/></svg><h3 class="product-title head-font">Our Products Six</h3><p class="product-copy">Lorem Ipsum is simply dummy text of the printing and typesetting industry. Lorem Ipsum has been the indus-try's standard dummy text ever since the 1500s, when an unknown printer took a galley of type and scrambled it to make a type specimen book. It has survived not only five centuries,</p><span class="more" style="text-decoration:none;top:120px">More</span></div>
<div class="abs rule" style="left:110px;top:805px;width:194px"></div><div class="abs rule" style="left:322px;top:805px;width:194px"></div>

<div class="product" style="left:106px;top:814px"><svg class="product-icon" viewBox="0 0 40 40"><rect x="8" y="6" width="22" height="28" rx="3" fill="#a4aab0"/><circle cx="16" cy="26" r="8" fill="#c6cbd0"/></svg><h3 class="product-title head-font" style="left:56px">Our Products Saven</h3><p class="product-copy" style="left:4px">Lorem Ipsum is simply dummy text of the printing and typesetting industry. Lorem Ipsum has been the indus-try's standard dummy text ever since the 1500s, when an unknown printer took a galley of type and scrambled it to make a type specimen book. It has survived not only five centuries,</p><span class="more" style="top:128px">More</span></div>
<div class="product" style="left:322px;top:814px"><svg class="product-icon" viewBox="0 0 40 40"><rect x="4" y="6" width="24" height="28" fill="#8a9096"/><circle cx="27" cy="29" r="8" fill="#5e646a"/></svg><h3 class="product-title head-font">Our Products Eight</h3><p class="product-copy">Lorem Ipsum is simply dummy text of the printing and typesetting industry. Lorem Ipsum has been the indus-try's standard dummy text ever since the 1500s, when an unknown printer took a galley of type and scrambled it to make a type specimen book. It has survived not only five centuries,</p><span class="more" style="top:128px">More</span></div>

<aside>
  <h2 class="abs sec-title head-font" style="left:552px;top:352px">Our Services</h2>
  <ul class="abs services">
    <li><svg width="10" height="10" viewBox="0 0 10 10"><circle cx="5" cy="5" r="4.3" fill="none" stroke="#555"/><path d="M4 3l2.2 2L4 7" fill="none" stroke="#555"/></svg>Lpsum is simply dummy text.</li>
    <li><svg width="10" height="10" viewBox="0 0 10 10"><circle cx="5" cy="5" r="4.3" fill="none" stroke="#555"/><path d="M4 3l2.2 2L4 7" fill="none" stroke="#555"/></svg>Scrambled it to make a type.</li>
    <li><svg width="10" height="10" viewBox="0 0 10 10"><circle cx="5" cy="5" r="4.3" fill="none" stroke="#555"/><path d="M4 3l2.2 2L4 7" fill="none" stroke="#555"/></svg>Printer took a galley .</li>
    <li><svg width="10" height="10" viewBox="0 0 10 10"><circle cx="5" cy="5" r="4.3" fill="none" stroke="#555"/><path d="M4 3l2.2 2L4 7" fill="none" stroke="#555"/></svg>Survived not only five centuries,</li>
    <li><svg width="10" height="10" viewBox="0 0 10 10"><circle cx="5" cy="5" r="4.3" fill="none" stroke="#555"/><path d="M4 3l2.2 2L4 7" fill="none" stroke="#555"/></svg>Unknown printer took a galley.</li>
    <li><svg width="10" height="10" viewBox="0 0 10 10"><circle cx="5" cy="5" r="4.3" fill="none" stroke="#555"/><path d="M4 3l2.2 2L4 7" fill="none" stroke="#555"/></svg>Lpsum is simply dummy text.</li>
    <li><svg width="10" height="10" viewBox="0 0 10 10"><circle cx="5" cy="5" r="4.3" fill="none" stroke="#555"/><path d="M4 3l2.2 2L4 7" fill="none" stroke="#555"/></svg>Scrambled it to make a type.</li>
    <li><svg width="10" height="10" viewBox="0 0 10 10"><circle cx="5" cy="5" r="4.3" fill="none" stroke="#555"/><path d="M4 3l2.2 2L4 7" fill="none" stroke="#555"/></svg>Printer took a galley.</li>
  </ul>

  <h2 class="abs sec-title head-font" style="left:552px;top:558px">Free Consultation</h2>
  <div class="abs form">
    <div class="field"><label>Name</label><i>*</i><span class="input"></span></div>
    <div class="field"><label>E-mail</label><i>*</i><span class="input"></span></div>
    <div class="field"><label>Zip-code</label><i>*</i><span class="input"></span></div>
    <div class="field"><label>Phone</label><i>*</i><span class="input"></span></div>
    <div class="field"><label>Service</label><i>*</i><span class="input select">New software<b><svg width="9" height="6" viewBox="0 0 9 6"><path d="M0 0h9L4.5 6z" fill="#1a7cc9"/></svg></b></span></div>
    <div class="field tall"><label>Message</label><i>*</i><span class="input"></span></div>
  </div>
  <div class="abs btn submit">Submit</div>

  <h2 class="abs sec-title head-font" style="left:552px;top:812px">Client Testimonials</h2>
  <svg class="abs" style="left:708px;top:815px" width="20" height="14" viewBox="0 0 20 14"><path d="M8 0v14L0 7z" fill="#1a7cc9"/><path d="M11 0v14l8-7z" fill="#9aa0a6"/></svg>
  <div class="abs testi-box">
    <div class="avatar" role="img" aria-label="Client avatar icon"></div>
    <span class="testi-name">Dr. Arvel Tomsen</span>
    <p class="testi-quote">"Lorem Ipsum is simply dummy text of the printing and typesetting industry. Lorem Ipsum has been the industry's standard It has survived not only five centuries"</p>
  </div>
</aside>

<section class="abs band"></section>
<h2 class="abs band-title" style="left:110px;top:987px">Clients Portfolio</h2>
<div class="abs tiles"><span></span><span></span><span></span><span></span><span></span><span></span></div>
<span class="abs more" style="left:278px;top:1130px">More</span>

<h2 class="abs band-title" style="left:337px;top:987px">Latest News &amp; Events</h2>
<div class="abs news-date" style="left:340px;top:1010px"><small>FEB</small><strong>5</strong></div>
<p class="abs news-copy" style="left:391px;top:1007px"><span style="color:var(--blue)">Lorem Ipsum</span> is simply dummy text of the printing and typeset-ting industry. Lorem Ipsum has been the industry</p>
<div class="abs news-date" style="left:340px;top:1068px"><small>FEB</small><strong>7</strong></div>
<p class="abs news-copy" style="left:391px;top:1065px">Lorem Ipsum is simply dummy text of the printing and typeset-ting industry. <span style="color:var(--blue)">Lorem Ipsum has been the industry</span></p>
<svg class="abs" style="left:492px;top:1122px" width="19" height="15" viewBox="0 0 19 15"><path d="M8 0v15L0 7.5z" fill="#1a7cc9"/><path d="M11 0v15l8-7.5z" fill="#9aa0a6"/></svg>

<h2 class="abs band-title" style="left:548px;top:987px">About Us</h2>
<p class="abs about-copy">Lorem Ipsum is simply dummy text of the printing and typesetting industry. Lorem Ipsum has been the industry's standard dummy text ever since the 1500s, when an unknown printer took a galley of type and scrambled it to make a type specimen book. It has survived not only five centuries,Lorem Ipsum is simply dummy text of the printing and typesetting industry. Lorem Ipsum has been the industry's standard dummy</p>
<span class="abs more" style="left:711px;top:1130px">More</span>

<footer class="abs footer"></footer>
<p class="abs copy">2013@ Allright Reserved.</p>
<span class="abs band-title sub-label">Subscribe to our newsletter</span>
<div class="abs sub-input">E-mail Address</div>
<div class="abs btn sub-btn">Subscribe</div>
</body>
</html>
```